Corvella Flood Restoration needing website

Hi Team

We are looking for a 4 or 5 page website containing
1: Home
2: Services
3: Gallery
4: Equipment Hire
5 Contact Us

Would want the front page to be a big call to action. Someones house has just flooded...they're highly stressed and we just want to let them know straight away that we can assist them

Some call to action would be great.

"Wet Carpets??"

"Washing machine just overflowed??"

"Burst pipe?"

"We're here to help!!"

Would be wanting a scrolling banner type homepage with images of flooded houses, heavy rain, a mother in shock that the house has been flooded by an overflowing washing machine, someone taking an emergency call with text saying that we are there to take your call 24/7 365 days a year

Target Market(s)

insurance companies and home owners

Industry/Entity Type

Hire

Coding

Coded - Design and coding required

Number of Pages Required

5+ page

Requirements
Must have
• 24/7 emergency contact number on home page (0468215937)
• 4 photos on banner on home page
• Equipment Hire Page should include images and brief description of these 3 products
• http://www.brintagesupply.com.au/item574.htm
• http://www.valdrix-tools.com.au/product/fresh-gust-fanunit/
• http://www.strellon.com.au/carpet/carpet-extractor-nomad-ser-i-ser-ii-ser-iii
• SERVICES OFFERED ARE:
• 24/7 Emergnecy Flood Restoration
• Insurance Claims
• Structural Drying
• Sub Floor Drying
• Supply and installation of drying equipment
• Professional Carpet and underlay installation
Nice to have
• Some other websites we like
• www.quillbyleakcare.com.au
• www.harrowdenrepairservices.com.au/flood-water-damage-restoration
• http://www.pelmarrecovery.com.au/
• http://www.drywellremedygroup.com.au/
Should not have
• not looking for an all white background.

```html
<!DOCTYPE html>
<html lang="en">
<head>
<meta charset="utf-8">
<title>Corvella Flood Restoration</title>
<link rel="stylesheet" href="https://fonts.googleapis.com/css2?family=Maven+Pro:wght@400;500;700&family=Roboto:wght@400;500&display=swap">
<style>
:root{
  --blue:#1a9ad6;
  --blue-dark:#0d7fbc;
  --blue-deep:#0b6ea6;
  --ink:#555;
  --ink-dark:#333;
  --grey-band:#d9d9d9;
  --footer:#232323;
  --footer-bottom:#1a1a1a;
  --white:#fff;
}
*{box-sizing:border-box;margin:0;padding:0}
html,body{width:1200px;height:2535px;overflow:hidden}
body{position:relative;font-family:"Roboto",sans-serif;color:var(--ink);background:var(--white)}

/* header */
.site-header{position:absolute;left:0;top:0;width:1200px;height:71px;background:var(--white);border-top:4px solid var(--blue)}
.brand{position:absolute;left:93px;top:14px;display:flex;align-items:center;gap:10px;color:var(--blue);font-family:"Maven Pro",sans-serif;font-weight:500;white-space:nowrap}
.brand-mark{width:34px;height:34px;border-radius:50%;background:var(--blue)}
.brand-name{line-height:1}
.brand-name .l1{display:block;font-size:27px;letter-spacing:1px}
.brand-name .l2{display:block;font-size:11px;letter-spacing:1.2px;margin-top:3px}
.main-nav{position:absolute;top:24px;left:389px;font-family:"Maven Pro",sans-serif;font-size:16px;color:#777}
.main-nav a{color:inherit;text-decoration:none;position:absolute;white-space:nowrap}
.main-nav .active{background:var(--blue);color:var(--white);padding:2px 10px;border-radius:2px;top:-2px}
.phone-tab{position:absolute;left:865px;top:0;width:242px;height:63px;background:var(--blue);border-radius:0 0 10px 30px;display:flex;align-items:center;gap:8px;padding-left:22px;color:var(--white);font-family:"Maven Pro",sans-serif;font-weight:500;font-size:24px;white-space:nowrap}
.phone-tab svg{flex:none}

/* hero */
.hero{position:absolute;left:0;top:71px;width:1200px;height:592px;background:linear-gradient(120deg,#1d4a63 0%,#3a7896 45%,#5c8ea6 70%,#274f66 100%)}
.hero-caption{position:absolute;left:225px;top:211px;width:748px;height:141px;background:rgba(16,48,78,.85);border-top:3px solid var(--blue);text-align:center;font-family:"Maven Pro",sans-serif;white-space:nowrap}
.hero-caption h1{font-weight:500;font-size:38px;color:var(--white);margin-top:34px;line-height:1}
.hero-caption p{font-size:29px;color:#2fb3ef;margin-top:6px}
.hero-arrow{position:absolute;top:264px;width:34px;height:67px;background:rgba(20,100,150,.8);color:var(--white);font-size:24px;display:flex;align-items:center;justify-content:center;font-family:"Maven Pro",sans-serif}
.hero-dots{position:absolute;left:575px;top:572px;display:flex;gap:4px}
.hero-dots span{width:9px;height:9px;border-radius:50%;border:1px solid var(--white)}
.hero-dots span.on{background:var(--white)}

/* welcome */
.welcome-title{position:absolute;left:0;top:725px;width:1200px;text-align:center;font-family:"Maven Pro",sans-serif;font-size:33px;color:#666;font-weight:400;white-space:nowrap}
.welcome-title strong{color:var(--blue);font-weight:700}
.welcome-title span{color:var(--blue)}
.title-rule{position:absolute;left:532px;top:777px;width:136px;height:3px;background:var(--blue)}
.welcome-text{position:absolute;left:101px;top:818px;width:998px;text-align:center;font-size:13.5px;line-height:27px;color:#666}
.emergency{position:absolute;left:262px;top:938px;display:flex;align-items:center;white-space:nowrap}
.emergency svg{flex:none}
.emergency-label{margin-left:6px;font-family:"Maven Pro",sans-serif;line-height:1}
.emergency-label .t1{display:block;font-size:23px;color:#666;letter-spacing:1px}
.emergency-label .t2{display:block;font-size:24px;color:var(--blue);font-weight:700;margin-top:3px;letter-spacing:-.2px}
.divider-v{position:absolute;left:593px;top:932px;height:94px;border-left:2px dashed #bbb}
.call-pill{position:absolute;left:617px;top:950px;width:262px;height:61px;background:var(--blue);border-radius:6px 0 0 30px;color:var(--white);font-family:"Maven Pro",sans-serif;padding:8px 0 0 16px;line-height:1;white-space:nowrap}
.call-pill .small{display:block;font-size:15px}
.call-pill .num{display:block;font-size:30px;font-weight:500;margin-top:3px}
.agent-photo{position:absolute;left:850px;top:938px;width:86px;height:86px;border-radius:50%;border:4px solid var(--blue);background:linear-gradient(160deg,#d9c8bb,#5a4a45)}

/* services */
.services{position:absolute;left:0;top:1100px;width:1200px;height:455px;background:linear-gradient(180deg,#1b9ad6 0%,#1788c6 55%,#1a97d4 100%);color:var(--white)}
.services h2{position:absolute;left:0;top:64px;width:1200px;text-align:center;font-family:"Maven Pro",sans-serif;font-size:33px;font-weight:400}
.services h2 strong{font-weight:700}
.services .intro{position:absolute;left:140px;top:126px;width:920px;text-align:center;font-size:13.5px;line-height:22px}
.service{position:absolute;top:230px;width:220px;margin-left:-110px;text-align:center;font-family:"Maven Pro",sans-serif;font-size:18px;line-height:20px;white-space:nowrap}
.service svg{display:block;margin:0 auto 12px}
.service.current{color:#bfe5f7}
.service-rule{position:absolute;top:255px;height:105px;border-left:1px dashed rgba(255,255,255,.5)}

/* gallery */
.gallery{position:absolute;left:0;top:1555px;width:1200px;height:690px;background:var(--grey-band)}
.gallery h2{position:absolute;left:0;top:72px;width:1200px;text-align:center;font-family:"Maven Pro",sans-serif;font-size:33px;font-weight:400;color:#666}
.gallery h2 strong{color:var(--blue);font-weight:700}
.view-all{position:absolute;left:997px;top:76px;width:110px;height:41px;border:2px solid var(--blue);color:var(--blue);font-family:"Maven Pro",sans-serif;font-weight:700;font-size:16px;display:flex;align-items:center;justify-content:center;background:var(--white)}
.tile{position:absolute}
.tile.living{left:93px;top:164px;width:319px;height:226px;background:linear-gradient(160deg,#5aa9cf,#2f7ea6)}
.tile.living::after{content:"";position:absolute;inset:10px;border:3px solid rgba(255,255,255,.85)}
.tile.house{left:421px;top:164px;width:356px;height:463px;background:linear-gradient(180deg,#a9d6ef 0%,#c9b6a4 35%,#7c6c5c 55%,#4f5f66 75%,#2f3b40 100%)}
.tile.stairs{left:786px;top:164px;width:321px;height:226px;background:linear-gradient(160deg,#d8d6d0,#7a756d 60%,#2f2c29)}
.tile.rain{left:93px;top:400px;width:319px;height:227px;background:linear-gradient(150deg,#5c8a3e,#8bb05a 50%,#c4577a)}
.tile.machine{left:786px;top:400px;width:321px;height:227px;background:linear-gradient(150deg,#d7ccbf,#9a9590 50%,#6f5a4a)}

/* footer */
.site-footer{position:absolute;left:0;top:2245px;width:1200px;height:226px;background:var(--footer);color:#bbb;font-size:12px}
.footer-brand{position:absolute;left:93px;top:60px;display:flex;align-items:center;gap:8px;color:var(--blue);font-family:"Maven Pro",sans-serif;font-weight:500;line-height:1;white-space:nowrap}
.footer-brand .mark{width:24px;height:24px;border-radius:50%;background:var(--blue)}
.footer-brand .l1{display:block;font-size:20px;letter-spacing:1px}
.footer-brand .l2{display:block;font-size:8px;letter-spacing:1px;margin-top:2px}
.socials{position:absolute;left:123px;top:106px;display:flex;gap:5px}
.socials span{width:27px;height:27px;background:#3b6ea8}
.footer-col h3{position:absolute;top:52px;font-family:"Maven Pro",sans-serif;font-size:14px;font-weight:500;color:var(--white);letter-spacing:.8px;white-space:nowrap}
.quick-links{position:absolute;left:350px;top:90px;list-style:none;line-height:26.5px;white-space:nowrap}
.contact-list{position:absolute;left:553px;top:88px;list-style:none;white-space:nowrap}
.contact-list li{display:flex;gap:12px;margin-bottom:14px;line-height:16px}
.contact-list svg{flex:none;margin-top:1px}
.newsletter-input{position:absolute;left:872px;top:91px;width:235px;height:40px;border:1px solid #555;display:flex;align-items:center;gap:8px;padding-left:10px;color:#777}
.newsletter-btn{position:absolute;left:872px;top:140px;width:128px;height:39px;background:var(--blue);color:var(--white);font-family:"Maven Pro",sans-serif;font-weight:700;font-size:15px;display:flex;align-items:center;justify-content:center}
.footer-bottom{position:absolute;left:0;top:2471px;width:1200px;height:64px;background:var(--footer-bottom);color:#ccc;font-size:12.5px;letter-spacing:1px;text-align:center;line-height:64px}
</style>
</head>
<body>

<header class="site-header">
  <div class="brand">
    <span class="brand-mark"></span>
    <span class="brand-name"><span class="l1">CORVELLA</span><span class="l2">FLOOD RESTORATION</span></span>
  </div>
  <nav class="main-nav">
    <a class="active" style="left:0">Home</a>
    <a style="left:79px">Services</a>
    <a style="left:164px">Gallery</a>
    <a style="left:241px">Equipment Hire</a>
    <a style="left:382px">Contact Us</a>
  </nav>
  <div class="phone-tab">
    <svg width="38" height="38" viewBox="0 0 40 40" aria-hidden="true"><circle cx="20" cy="20" r="17" fill="none" stroke="#fff" stroke-width="2.5"/><text x="20" y="25" text-anchor="middle" font-family="Maven Pro, sans-serif" font-size="13" font-weight="700" fill="#fff">24/7</text></svg>
    <span>046 8215 937</span>
  </div>
</header>

<section class="hero" role="img" aria-label="Banner photo: a mother in a laundry room shocked by an overflowing washing machine, water across the floor">
  <div class="hero-arrow" style="left:0">&gt;</div>
  <div class="hero-arrow" style="right:0">&gt;</div>
  <div class="hero-caption">
    <h1>Washing machine just overflowed??</h1>
    <p>We're here to help!!</p>
  </div>
  <div class="hero-dots"><span class="on"></span><span></span><span></span><span></span></div>
</section>

<h2 class="welcome-title">Welcome to <strong>CORVELLA</strong> <span>Flood Restoration</span></h2>
<div class="title-rule"></div>
<p class="welcome-text">Lorem ipsum dolor sit amet, consectetur adipiscing edu e elit, sed do eiusmod tempor incididunt labore et dolore magna aliqua. Ut enim minim veniam, quis nostrud exercitation ullamco laboris nisi ut aliquip erex ea commodo consequat. Duis aut irure dolor in reprehendit in voluptate velit esse cillum dolore eu fugiat nulla pariatur. Excepteur sin in occacecat cupidatat non prident, edu sunt in culpa qui officia deserunt laboris nisi ut consectetur adipiscing edu.</p>

<div class="emergency">
  <svg width="84" height="84" viewBox="0 0 88 86" aria-hidden="true">
    <path d="M20 14 A36 36 0 1 1 14 66" fill="none" stroke="#1a9ad6" stroke-width="4"/>
    <path d="M8 50 q-4 -14 8 -20 l6 10 q-6 4 -2 12 q4 8 12 6 l6 10 q-14 10 -30 -18z" fill="#1a9ad6"/>
    <text x="47" y="50" text-anchor="middle" font-family="Maven Pro, sans-serif" font-size="20" font-weight="700" fill="#555">24/7</text>
  </svg>
  <div class="emergency-label"><span class="t1">24/7 Emergnecy</span><span class="t2">Flood Restoration</span></div>
</div>
<div class="divider-v"></div>
<div class="call-pill"><span class="small">CALL US ON</span><span class="num">046 8215 937</span></div>
<div class="agent-photo" role="img" aria-label="Photo of a customer service agent wearing a headset"></div>

<section class="services">
  <h2>Our <strong>Services</strong></h2>
  <p class="intro">Lorem ipsum dolor sit amet, consectetur adipiscing edu e elit, sed do eiusmod tempor incididunt ut labore et dolore magna aliqua. Ut enim minim veniam, quis nostrud exercitation ullamco laboris nisi ut psum dolor sit amet, consectetur adipiscing edu e elit</p>

  <div class="service" style="left:152px">
    <svg width="86" height="80" viewBox="0 0 86 80" aria-hidden="true"><path d="M6 40 Q20 4 60 8 Q82 14 80 40 Q70 32 58 38 Q50 28 40 36 Q28 26 18 40 Q12 34 6 40z" fill="#fff"/><path d="M44 34 L58 74 q2 6 -4 6" fill="none" stroke="#fff" stroke-width="4" stroke-linecap="round"/></svg>
    Insurance<br>Claims
  </div>
  <div class="service-rule" style="left:250px"></div>
  <div class="service" style="left:355px">
    <svg width="72" height="80" viewBox="0 0 72 80" aria-hidden="true"><rect x="6" y="18" width="26" height="62" fill="#fff"/><rect x="16" y="4" width="8" height="14" fill="#fff"/><rect x="36" y="36" width="30" height="44" fill="#fff"/><g fill="#1788c6"><rect x="11" y="26" width="5" height="7"/><rect x="22" y="26" width="5" height="7"/><rect x="11" y="40" width="5" height="7"/><rect x="22" y="40" width="5" height="7"/><rect x="11" y="54" width="5" height="7"/><rect x="22" y="54" width="5" height="7"/><rect x="42" y="44" width="6" height="7"/><rect x="54" y="44" width="6" height="7"/><rect x="42" y="58" width="6" height="7"/><rect x="54" y="58" width="6" height="7"/></g></svg>
    Structural<br>Drying
  </div>
  <div class="service-rule" style="left:443px"></div>
  <div class="service current" style="left:541px">
    <svg width="96" height="80" viewBox="0 0 96 80" aria-hidden="true"><path d="M22 16 H74 L92 76 H4z" fill="none" stroke="#fff" stroke-width="4"/><path d="M32 26 H64 L70 52 H26z" fill="#fff"/><line x1="4" y1="62" x2="92" y2="62" stroke="#fff" stroke-width="3"/></svg>
    Sub Floor<br>Drying
  </div>
  <div class="service-rule" style="left:629px"></div>
  <div class="service" style="left:766px">
    <svg width="92" height="80" viewBox="0 0 92 80" aria-hidden="true"><rect x="2" y="12" width="8" height="3" fill="#fff"/><rect x="2" y="20" width="12" height="3" fill="#fff"/><rect x="2" y="28" width="8" height="3" fill="#fff"/><path d="M16 8 H62 A18 18 0 0 1 62 44 H52 L56 74 H40 L36 44 H16z" fill="#fff"/><circle cx="64" cy="26" r="11" fill="#1788c6"/><circle cx="64" cy="26" r="5" fill="#fff"/></svg>
    Supply &amp; installation of<br>drying equipment
  </div>
  <div class="service-rule" style="left:896px"></div>
  <div class="service" style="left:1014px">
    <svg width="92" height="80" viewBox="0 0 92 80" aria-hidden="true"><path d="M10 58 L62 8 L88 30 L36 78z" fill="none" stroke="#fff" stroke-width="4"/><circle cx="22" cy="46" r="14" fill="#fff"/><path d="M22 32 L70 10 L84 24 L34 58z" fill="#fff"/><circle cx="22" cy="46" r="5" fill="#1788c6"/></svg>
    Professional Carpet &amp;<br>underlay installation
  </div>
</section>

<section class="gallery">
  <h2>Our <strong>Gallery</strong></h2>
  <div class="view-all">View All</div>
  <div class="tile living" role="img" aria-label="Photo of a flooded blue living room with a sofa"></div>
  <div class="tile house" role="img" aria-label="Photo of a brick house surrounded by flood water"></div>
  <div class="tile stairs" role="img" aria-label="Photo of a flooded hallway and staircase"></div>
  <div class="tile rain" role="img" aria-label="Photo of a person under a colourful umbrella in heavy rain"></div>
  <div class="tile machine" role="img" aria-label="Photo of a carpet cleaning machine on a rug"></div>
</section>

<footer class="site-footer">
  <div class="footer-brand">
    <span class="mark"></span>
    <span><span class="l1">CORVELLA</span><span class="l2">FLOOD RESTORATION</span></span>
  </div>
  <div class="socials" aria-label="Social links"><span></span><span></span><span></span><span></span></div>

  <div class="footer-col"><h3 style="left:350px">QUICK LINKS</h3></div>
  <ul class="quick-links">
    <li>&gt;&gt; Home</li>
    <li>&gt;&gt; Services</li>
    <li>&gt;&gt; Gallery</li>
    <li>&gt;&gt; Equipment Hire</li>
  </ul>

  <div class="footer-col"><h3 style="left:553px">CONTACT US</h3></div>
  <ul class="contact-list">
    <li><svg width="12" height="14" viewBox="0 0 12 14" aria-hidden="true"><path d="M6 0 A5 5 0 0 1 11 5 C11 9 6 14 6 14 C6 14 1 9 1 5 A5 5 0 0 1 6 0z" fill="#ccc"/><circle cx="6" cy="5" r="2" fill="#232323"/></svg><span>48 Harbour Lane<br>Township Name, NY 08096</span></li>
    <li><svg width="12" height="12" viewBox="0 0 12 12" aria-hidden="true"><path d="M2 0 L4.5 3 L3 5 Q4.5 7.5 7 9 L9 7.5 L12 10 L10 12 Q4 11.5 0 2z" fill="#ccc"/></svg><span>046 8215 937</span></li>
    <li><svg width="12" height="10" viewBox="0 0 12 10" aria-hidden="true"><rect width="12" height="10" fill="#ccc"/><path d="M0 0 L6 5 L12 0" fill="none" stroke="#232323" stroke-width="1.2"/></svg><span>customerservice@corvella.com</span></li>
  </ul>

  <div class="footer-col"><h3 style="left:872px">SUBSCRIBE OUR NEWSLETTER</h3></div>
  <div class="newsletter-input"><svg width="12" height="10" viewBox="0 0 12 10" aria-hidden="true"><rect width="12" height="10" fill="#777"/><path d="M0 0 L6 5 L12 0" fill="none" stroke="#232323" stroke-width="1.2"/></svg>Email</div>
  <div class="newsletter-btn">Submit</div>
</footer>
<div class="footer-bottom">© Corvella Flood Restoration.&nbsp; All rights reserved.</div>

</body>
</html>
```